brimwood
business cards & stationary
Modern
marcus tolley
director
Brimwood Carpentry Limited
Unit 4 & 6 fenwick trade estate, fenwick, holbrook, ashdale, sk14 7pj
marcus@brimwoodcarpentry.co.uk
www.brimwoodcarpentry.co.uk
I would like the business card to be printed on thick matte black card. I think it would be interesting if the text was printed in silver leaf.
I would like to perhaps see the employee name in all lower case.
Please introduce keywords... architectural joinery ~ bespoke furniture - design somewhere on the card perhaps on back at bottom.
Logo
Web address
Keywords
photo shows a card I like

```html
<!DOCTYPE html>
<html lang="en">
<head>
<meta charset="utf-8">
<title>brimwood — stationery</title>
<link rel="stylesheet" href="https://fonts.googleapis.com/css2?family=Questrial&display=swap">
<style>
  :root {
    --paper: #ffffff;
    --ink: #1c1c1c;
    --card: #161616;
    --silver: #d9d9d9;
    --mute: #8a8a8a;
    --ghost: #e6e6e6;
    --tile-light: #cfcfcf;
    --stage: #ffffff;
  }
  * { margin: 0; padding: 0; box-sizing: border-box; }
  html, body { width: 1200px; height: 847px; overflow: hidden; background: var(--stage); }
  body { font-family: "Questrial", "Helvetica Neue", Arial, sans-serif; color: var(--ink); position: relative; }
  address { font-style: normal; }

  .sheet { position: absolute; background: var(--paper); box-shadow: 0 2px 6px rgba(0,0,0,.18); overflow: hidden; }

  .brand-tile { position: absolute; background: var(--card); display: flex; align-items: flex-end; justify-content: center; }
  .brand-tile span { color: var(--paper); font-size: 15px; letter-spacing: 2px; margin-bottom: 12px; }

  .ghost-name { position: absolute; color: var(--ghost); letter-spacing: 2px; white-space: nowrap; line-height: 1; }

  .contact { position: absolute; font-size: 8px; line-height: 1.6; color: #444; white-space: nowrap; }

  /* envelope */
  .envelope { left: 72px; top: 60px; width: 504px; height: 276px; }
  .envelope .flap { position: absolute; left: 0; top: 0; width: 504px; height: 34px; }
  .envelope .flap-web { position: absolute; top: 12px; left: 0; width: 100%; text-align: center; font-size: 6px; letter-spacing: 3px; color: var(--mute); }
  .envelope .rule { position: absolute; left: 0; top: 34px; width: 100%; height: 8px; background: var(--card); }
  .envelope .brand-tile { left: 20px; top: 84px; width: 90px; height: 112px; }
  .envelope .ghost-name { left: 138px; top: 132px; font-size: 66px; }
  .envelope .keywords-vertical { position: absolute; left: 4px; top: 250px; transform: rotate(-90deg); transform-origin: left top; font-size: 7px; letter-spacing: 3px; color: var(--mute); white-space: nowrap; }
  .envelope .contact { left: 20px; top: 208px; }

  /* letterhead */
  .letterhead { left: 600px; top: 29px; width: 528px; height: 763px; }
  .letterhead .brand-tile { left: 12px; top: 7px; width: 88px; height: 108px; }
  .letterhead .contact { left: 120px; top: 118px; }
  .letterhead .ghost-name { left: 20px; top: 330px; font-size: 104px; }
  .letterhead .footer-band { position: absolute; left: 0; bottom: 0; width: 100%; height: 41px; background: var(--card); display: flex; align-items: center; justify-content: center; }
  .footer-band span { color: var(--silver); font-size: 8px; letter-spacing: 4px; }

  /* cards */
  .card { position: absolute; background: var(--card); box-shadow: 0 3px 8px rgba(0,0,0,.3); color: var(--silver); }
  .card-back { left: 348px; top: 480px; width: 444px; height: 197px; }
  .card-back .face { position: absolute; left: 140px; right: 0; top: 70px; text-align: center; }
  .card-back .wordmark { font-size: 26px; letter-spacing: 6px; color: var(--paper); }
  .card-back .keywords { margin-top: 14px; color: var(--silver); font-size: 7px; letter-spacing: 2.4px; white-space: nowrap; }
  .card-front { left: 48px; top: 547px; width: 432px; height: 197px; }
  .card-front .brand-tile { left: 5px; top: 5px; width: 106px; height: 106px; background: var(--tile-light); }
  .card-front .brand-tile span { color: var(--card); }
  .card-front .person { position: absolute; left: 16px; top: 122px; }
  .person .name { font-size: 11px; color: var(--paper); letter-spacing: .5px; }
  .person .role { font-size: 7px; color: var(--mute); margin-bottom: 8px; }
  .person .details { font-size: 7px; line-height: 1.5; color: var(--silver); white-space: nowrap; }
</style>
</head>
<body>

<section class="sheet envelope" aria-label="DL envelope">
  <svg class="flap" viewBox="0 0 504 34" aria-hidden="true">
    <polygon points="0,0 504,0 504,34 0,34" fill="#fafafa" stroke="#dcdcdc"/>
  </svg>
  <div class="flap-web">www.brimwoodcarpentry.co.uk</div>
  <div class="rule"></div>
  <div class="ghost-name" aria-hidden="true">brimwood</div>
  <div class="keywords-vertical">architectural joinery ~ bespoke furniture</div>
  <div class="brand-tile"><span>brimwood</span></div>
  <address class="contact">
    Brimwood Carpentry Limited<br>
    Unit 4 &amp; 6 fenwick trade estate, fenwick, holbrook, ashdale, sk14 7pj<br>
    T: +44 (0)1625 480 317 | M: 07700 914 562 | E: marcus@brimwoodcarpentry.co.uk
  </address>
</section>

<section class="sheet letterhead" aria-label="Letterhead">
  <div class="brand-tile"><span>brimwood</span></div>
  <address class="contact">
    Brimwood Carpentry Limited<br>
    Unit 4 &amp; 6 fenwick trade estate, fenwick, holbrook, ashdale, sk14 7pj<br>
    T: +44 (0)1625 480 317 | M: 07700 914 562<br>
    E: marcus@brimwoodcarpentry.co.uk | www.brimwoodcarpentry.co.uk
  </address>
  <div class="ghost-name" aria-hidden="true">brimwood</div>
  <div class="footer-band"><span>architectural joinery ~ bespoke furniture</span></div>
</section>

<section class="card card-back" aria-label="Business card, reverse">
  <div class="face">
    <div class="wordmark">brimwood</div>
    <div class="keywords">architectural joinery ~ bespoke furniture</div>
  </div>
</section>

<section class="card card-front" aria-label="Business card, front">
  <div class="brand-tile"><span>brimwood</span></div>
  <div class="person">
    <p class="name">marcus tolley</p>
    <p class="role">director</p>
    <address class="details">
      Brimwood Carpentry Limited<br>
      Unit 4 &amp; 6 fenwick trade estate, fenwick, holbrook, ashdale, sk14 7pj<br>
      T: +44 (0)1625 480 317 | M: 07700 914 562<br>
      E: marcus@brimwoodcarpentry.co.uk | www.brimwoodcarpentry.co.uk
    </address>
  </div>
</section>

</body>
</html>
```